Casino with the 'highest winning percentage' needs a stationery design

This is for a casino in Colombo, Sri Lanka and we need a stationery design for business card, letter head and envelope.

Should be very professional, simple and elegant without fancy fonts

Reason: Not fully satisfied with the designs. Need more designs.

Industry/Entity Type

Business

Requirements
Must have
• 1. card deck symbol 'CLUBS' in red, or black

2. name in BLOCK CAPITAL LETTERS

3. Preferred font colours are black, white or red

4. Prefer 'professional /elegant' fonts
Should not have
• SHOULD NOT HAVE ANY OTHER SYMBOL EXCEPT 'CLUBS'

DO NOT PREFER ITALIC FONTS

```html
<!DOCTYPE html>
<html lang="en">
<head>
<meta charset="utf-8">
<title>Marlow's Entertainment – Business Card</title>
<link href="https://fonts.googleapis.com/css2?family=Noto+Serif:wght@400;700&display=swap" rel="stylesheet">
<style>
  :root {
    --red: #d42f38;
    --red-soft: rgba(255, 255, 255, 0.1);
    --ink: #111111;
    --paper: #ffffff;
    --backdrop: #ece8e3;
    --rule: #c9c9c9;
  }
  * { margin: 0; padding: 0; box-sizing: border-box; }
  html, body { width: 1200px; height: 372px; overflow: hidden; }
  body {
    background: var(--backdrop);
    font-family: "Noto Serif", Georgia, serif;
    position: relative;
  }
  .card {
    position: absolute;
    top: 27px;
    width: 557px;
    height: 318px;
    overflow: hidden;
    box-shadow: 0 1px 4px rgba(0,0,0,0.25);
  }
  .card--front { left: 37px; background: var(--paper); }
  .card--back { left: 622px; background: var(--red); }

  .brand-mark {
    position: absolute;
    border-radius: 50%;
  }
  .card--front .brand-mark { left: 122px; top: 52px; width: 66px; height: 66px; background: var(--red); }
  .card--back .brand-mark { left: 106px; top: 124px; width: 66px; height: 66px; background: var(--paper); }

  .brand-name {
    position: absolute;
    font-weight: 700;
    font-size: 27px;
    line-height: 35px;
    letter-spacing: 0.3px;
  }
  .card--front .brand-name { left: 212px; top: 50px; color: var(--ink); }
  .card--back .brand-name { left: 196px; top: 117px; color: var(--paper); }

  .company {
    position: absolute;
    right: 288px;
    top: 160px;
    text-align: right;
    color: var(--ink);
    font-size: 13px;
    line-height: 19px;
  }
  .company__name {
    color: var(--red);
    font-weight: 700;
    font-size: 15.5px;
    margin-bottom: 9px;
    letter-spacing: 0.2px;
  }
  .divider {
    position: absolute;
    left: 284px;
    top: 160px;
    width: 1px;
    height: 98px;
    background: var(--rule);
  }
  .contacts {
    position: absolute;
    left: 302px;
    top: 168px;
    list-style: none;
    font-size: 13px;
    color: var(--ink);
  }
  .contacts li { display: flex; align-items: center; height: 21px; }
  .contacts svg { width: 11px; height: 11px; margin-right: 7px; fill: var(--red); }

  .footer-rule {
    position: absolute;
    left: 0; right: 0;
    top: 284px;
    height: 2px;
    background: var(--ink);
  }
  .footer-band {
    position: absolute;
    left: 0; right: 0;
    top: 291px;
    bottom: 0;
    background: var(--red);
    color: var(--paper);
    font-size: 13px;
    letter-spacing: 3px;
    text-align: center;
    line-height: 27px;
  }

  .suit-pattern {
    position: absolute;
    left: 142px;
    top: 10px;
    width: 347px;
    height: 308px;
    background: var(--red-soft);
    border-radius: 40px;
  }
  .tagline {
    position: absolute;
    left: 0; right: 0;
    top: 238px;
    text-align: center;
    color: var(--paper);
    font-weight: 700;
    font-size: 15px;
    letter-spacing: 1.6px;
  }
</style>
</head>
<body>

<section class="card card--front">
  <span class="brand-mark" aria-hidden="true"></span>
  <h1 class="brand-name">MARLOW’S<br>ENTERTAINMENT</h1>

  <address class="company" style="font-style:normal">
    <div class="company__name">MARLOW’S LIMITED</div>
    18, Lotus Garden Road<br>
    Colombo 01000<br>
    Sri Lanka
  </address>

  <span class="divider" aria-hidden="true"></span>

  <ul class="contacts">
    <li>
      <svg viewBox="0 0 12 12" aria-label="Telephone"><path d="M2.5 0.8 4.3 0.6 5.2 3.3 3.9 4.2C4.5 5.6 6.2 7.4 7.7 8.1L8.6 6.8 11.3 7.7 11.1 9.5C10.9 10.7 9.8 11.3 8.7 11 4.8 9.9 1.9 7 0.9 3.2 0.6 2.1 1.3 1 2.5 0.8Z"/></svg>
      + 94 11 2450178
    </li>
    <li>
      <svg viewBox="0 0 12 12" aria-label="Mobile"><path d="M3 0h6a1 1 0 0 1 1 1v10a1 1 0 0 1-1 1H3a1 1 0 0 1-1-1V1a1 1 0 0 1 1-1Zm0.6 1.4v7.4h4.8V1.4Z"/></svg>
      + 94 77 0000000
    </li>
    <li>
      <svg viewBox="0 0 12 12" aria-label="Fax"><path d="M3 0h6v3H3Zm-2 4h10a1 1 0 0 1 1 1v5H0V5a1 1 0 0 1 1-1Zm2 3v5h6V7Z"/></svg>
      + 94 11 0000000
    </li>
    <li>
      <svg viewBox="0 0 12 12" aria-label="Email"><path d="M0 2h12v8H0Zm1.2 1.1v0.4L6 6.6l4.8-3.1v-0.4Z"/></svg>
      info@marlowscolombo.com
    </li>
  </ul>

  <span class="footer-rule" aria-hidden="true"></span>
  <div class="footer-band">www.marlowscolombo.com</div>
</section>

<section class="card card--back">
  <div class="suit-pattern" role="img" aria-label="Faint card-suit pattern in lighter red"></div>
  <span class="brand-mark" aria-hidden="true"></span>
  <h2 class="brand-name">MARLOW’S<br>ENTERTAINMENT</h2>
  <p class="tagline">Highest Winning Percentage In The World</p>
</section>

</body>
</html>
```